Business Card Design for an international medical business

We need a professional and elegant business card design with fashionable graphic element. Our company is located in Hong Kong with three worldwide production lines for medical equipment(surgical face masks, N95, face shields and so on). Our factories all contain medical standard ISOs and all product fulfill Garrow lab and KTR testing standards.

We would like to see designs that show the impression of our professional expertise, formal corporate image with creative thinking work style and inspiring global concept. We want the content in both English and Japanese on the same card. We also want to print our the patent trade mark and company logo on the card.

Target Market(s)

Southeast Asia, US, EU

Industry/Entity Type

Medical Equipment

Contact Information for Business Card

Below are the content we want to be shown on the business card(please help us to simplified them to be more presentable and readable):

Company name: Brightmoor (Hong Kong) 5K Medical Technology Company Limited
Address: Unit 2204, 22/F, Pine Court, No.8 Ferndale Road, Kwun Lam, Hong Kong.
Band Name: B5K
Homepage: www.brightmoor5kq.com
Name: Lok Wing Fei
Title: Manager
Tel: +852-xxxx-xxxx
Mobile: +852-xxxx-xxxx
Email: xx@brightmoor5kq.com

Production Lines:
China: Ping Shan Kai Lok Medical Technology Company Limited
Mo Tan City Ren Bo Textile Machinery Company Limited
Bangladesh: B5K Medical Technology Company Limited

Qualifications:
ISO 13485:2016
ISO 14644-1:2015
ISO Class 8 Cleanroom
ASTM F2100 Level 2
EN14683 Type IIR
EN149 FFP2
CE Certified
FDA Registration number: XXX

Requirements
Must have
• use pantone color for the design
and provide the pantone number for printing purpose
Should not have
• Background color should not be black.

```html
<!DOCTYPE html>
<html lang="en">
<head>
<meta charset="utf-8">
<title>Brightmoor Business Card</title>
<link href="https://fonts.googleapis.com/css2?family=Source+Sans+3:wght@400;600;700&display=swap" rel="stylesheet">
<style>
  :root {
    --pink: #e8194f;
    --teal: #2fb3b0;
    --paper: #ffffff;
    --backdrop: #e9ecef;
    --ink-shadow: rgba(30, 40, 50, 0.18);
  }
  * { box-sizing: border-box; margin: 0; padding: 0; }
  html, body { width: 1200px; height: 900px; overflow: hidden; }
  body {
    background: var(--backdrop);
    font-family: "Source Sans 3", sans-serif;
    display: flex;
    flex-direction: column;
    align-items: center;
    justify-content: center;
    gap: 40px;
  }
  .card {
    position: relative;
    width: 700px;
    height: 400px;
    background: var(--paper);
    box-shadow: 0 6px 20px var(--ink-shadow);
    overflow: hidden;
  }

  /* Front */
  .brand {
    position: absolute;
    top: 40px;
    right: 50px;
    display: flex;
    align-items: center;
    gap: 12px;
  }
  .brand-dot {
    width: 22px; height: 22px;
    border-radius: 50%;
    background: var(--pink);
  }
  .brand-text { display: flex; flex-direction: column; }
  .brand-name {
    font-size: 44px;
    font-weight: 700;
    color: var(--pink);
    letter-spacing: 1px;
    line-height: 1;
  }
  .brand-sub {
    font-size: 11px;
    font-weight: 600;
    color: var(--teal);
    margin-top: 4px;
    text-align: right;
  }
  .person {
    position: absolute;
    top: 118px;
    left: 60px;
  }
  .person-name {
    font-size: 30px;
    font-weight: 700;
    color: var(--pink);
    letter-spacing: 0.5px;
  }
  .person-title {
    font-size: 16px;
    font-weight: 600;
    color: var(--teal);
  }
  .divider {
    position: absolute;
    left: 360px;
    top: 160px;
    width: 2px;
    height: 80px;
    background: var(--teal);
  }
  .contacts {
    position: absolute;
    left: 390px;
    top: 155px;
    list-style: none;
  }
  .contacts li {
    display: flex;
    align-items: center;
    gap: 10px;
    font-size: 15px;
    color: var(--pink);
    height: 24px;
  }
  .contacts svg { width: 16px; height: 16px; flex: none; }
  .address-band {
    position: absolute;
    left: 0; right: 0;
    top: 300px;
    height: 40px;
    background: var(--pink);
    color: var(--paper);
    font-size: 15px;
    font-weight: 600;
    display: flex;
    align-items: center;
    padding-left: 60px;
  }

  /* Back */
  .section-title {
    position: absolute;
    font-size: 24px;
    font-weight: 700;
    color: var(--pink);
  }
  .lines-title { top: 26px; left: 260px; }
  .quals-title { top: 160px; left: 260px; }
  .lines {
    position: absolute;
    top: 66px;
    left: 50px;
    display: grid;
    grid-template-columns: 100px auto;
    row-gap: 2px;
    font-size: 15px;
  }
  .lines dt { color: var(--pink); font-weight: 600; }
  .lines dd { color: var(--teal); }
  .quals {
    position: absolute;
    top: 202px;
    left: 50px;
    list-style: none;
    display: grid;
    grid-template-columns: 200px 210px 200px;
    row-gap: 8px;
  }
  .quals li {
    display: flex;
    align-items: center;
    gap: 8px;
    font-size: 15px;
    color: var(--teal);
  }
  .quals svg { width: 16px; height: 14px; flex: none; }
  .fda-band {
    position: absolute;
    left: 0;
    top: 320px;
    width: 290px;
    height: 36px;
    background: var(--pink);
    color: var(--paper);
    font-size: 16px;
    font-weight: 600;
    display: flex;
    align-items: center;
    padding-left: 30px;
  }
  .back-brand {
    position: absolute;
    right: 50px;
    bottom: 36px;
    display: flex;
    align-items: center;
    gap: 10px;
  }
  .back-brand .brand-dot { width: 18px; height: 18px; }
  .back-brand-name {
    font-size: 40px;
    font-weight: 700;
    color: var(--pink);
    line-height: 1;
  }
</style>
</head>
<body>

<section class="card card-front">
  <div class="brand">
    <span class="brand-dot"></span>
    <div class="brand-text">
      <span class="brand-name">BRIGHTMOOR</span>
      <span class="brand-sub">5K Medical Technology Company Limited</span>
    </div>
  </div>

  <div class="person">
    <h1 class="person-name">LOK WING FEI</h1>
    <p class="person-title">Manager</p>
  </div>

  <span class="divider"></span>

  <ul class="contacts">
    <li>
      <svg viewBox="0 0 16 16" fill="none" stroke="var(--teal)" stroke-width="1.4"><rect x="4" y="1" width="8" height="14" rx="1.5"/><line x1="7" y1="12.5" x2="9" y2="12.5"/></svg>
      +852-xxxx-xxxx
    </li>
    <li>
      <svg viewBox="0 0 16 16" fill="none" stroke="var(--teal)" stroke-width="1.4"><path d="M3 2h3l1.5 3.5-2 1.2a8 8 0 0 0 3.8 3.8l1.2-2L14 10v3a1 1 0 0 1-1 1A12 12 0 0 1 2 3a1 1 0 0 1 1-1z"/></svg>
      +852-xxxx-xxxx
    </li>
    <li>
      <svg viewBox="0 0 16 16" fill="none" stroke="var(--teal)" stroke-width="1.3"><circle cx="8" cy="8" r="6.5"/><ellipse cx="8" cy="8" rx="3" ry="6.5"/><line x1="1.5" y1="8" x2="14.5" y2="8"/></svg>
      www.brightmoor5kq.com
    </li>
    <li>
      <svg viewBox="0 0 16 16" fill="none" stroke="var(--teal)" stroke-width="1.4"><rect x="1.5" y="3.5" width="13" height="9" rx="1"/><path d="M1.5 4l6.5 5 6.5-5"/></svg>
      xx@brightmoor5kq.com
    </li>
  </ul>

  <div class="address-band">Unit 2204, 22/F, Pine Court, No.8 Ferndale Road, Kwun Lam, Hong Kong</div>
</section>

<section class="card card-back">
  <h2 class="section-title lines-title">Production Lines:</h2>
  <dl class="lines">
    <dt>China:</dt>
    <dd>Ping Shan Kai Lok Medical Technology Company Limited</dd>
    <dt></dt>
    <dd>Mo Tan City Ren Bo Textile Machinery Company Limited</dd>
    <dt>Bangladesh:</dt>
    <dd>B5K Medical Technology Company Limited</dd>
  </dl>

  <h2 class="section-title quals-title">Qualifications:</h2>
  <ul class="quals">
    <li><svg viewBox="0 0 16 14"><rect x="0.5" y="2.5" width="10" height="10" fill="none" stroke="var(--pink)"/><path d="M3 7l3 3 9-9" fill="none" stroke="var(--teal)" stroke-width="2"/></svg>ISO 13485:2016</li>
    <li><svg viewBox="0 0 16 14"><rect x="0.5" y="2.5" width="10" height="10" fill="none" stroke="var(--pink)"/><path d="M3 7l3 3 9-9" fill="none" stroke="var(--teal)" stroke-width="2"/></svg>ISO 14644-1:2015</li>
    <li><svg viewBox="0 0 16 14"><rect x="0.5" y="2.5" width="10" height="10" fill="none" stroke="var(--pink)"/><path d="M3 7l3 3 9-9" fill="none" stroke="var(--teal)" stroke-width="2"/></svg>ISO Class 8 Cleanroom</li>
    <li><svg viewBox="0 0 16 14"><rect x="0.5" y="2.5" width="10" height="10" fill="none" stroke="var(--pink)"/><path d="M3 7l3 3 9-9" fill="none" stroke="var(--teal)" stroke-width="2"/></svg>ASTM F2100 Level 2</li>
    <li><svg viewBox="0 0 16 14"><rect x="0.5" y="2.5" width="10" height="10" fill="none" stroke="var(--pink)"/><path d="M3 7l3 3 9-9" fill="none" stroke="var(--teal)" stroke-width="2"/></svg>EN14683 Type IIR</li>
    <li><svg viewBox="0 0 16 14"><rect x="0.5" y="2.5" width="10" height="10" fill="none" stroke="var(--pink)"/><path d="M3 7l3 3 9-9" fill="none" stroke="var(--teal)" stroke-width="2"/></svg>EN149 FFP2</li>
    <li><svg viewBox="0 0 16 14"><rect x="0.5" y="2.5" width="10" height="10" fill="none" stroke="var(--pink)"/><path d="M3 7l3 3 9-9" fill="none" stroke="var(--teal)" stroke-width="2"/></svg>CE Certified</li>
  </ul>

  <div class="fda-band">FDA Registration number: XXX</div>

  <div class="back-brand">
    <span class="brand-dot"></span>
    <span class="back-brand-name">B5K</span>
  </div>
</section>

</body>
</html>
```